Shelter is Kindred Warmth Fact Sheet (2 sided page)

We are looking to create a 2-page Fact Sheet (front and back)
- The head logo is going to be: Shelter is Kindred Warmth
- The title of the fact sheet will be: Get the Facts on Mpox Vaccination
- Please include RK7's logo - please make sure there is room for another logo next to this (this is not included at this time)
- Use the colors and font and mimic the feel of our past resources from ravenkinship.org/resources
- The main image should be incorporated for design (this is the beading circle image with 3 people beading) - additional images (feather & braided sweetgrass) can be included as needed for elements
- Do not put text over graphics and keep it simple and easy to read with high contrast.
- We want some very simple design element(s) incorporated that convey Native American communities or heritage. But NO headdress, teepee graphics, etc.
- Ensure that linked text remains in document for virtual use
- Please include this list before the funding statement - For more information, please visit:
www.ravenkinship.org/vaccines
www.bolderpath.org/campaigns/mpox/
www.nwho.example/poxvirus/mpox/
- Please remember to include the funding statement - it can be in a very small font 6/7 point. "This project: Joining Hands with Regional Allies to Strengthen Neighborhood-Led Groups to Broaden Immunization Reach Among Diverse Cultural and Heritage Grown-Up Groups Presently Facing Gaps is supported by the Bureau for Illness Tracking and Safeguarding (BITS) of the Federal Office of Wellness and Social Services (OWS) as part of a financial assistance award totaling $5,000,000 with 100 percent funded by BITS/OWS. The contents are those of the author(s) and do not necessarily represent the official views of, nor an endorsement by, BITS/OWS or the Northland Federal Government. "

Target Market(s)

American Indian and Alaska Native Two Spirit Indigiqueer

Requirements
Must have
• Worldwide Council for Native Elders (RK7) color scheme - see website

```html
<!DOCTYPE html>
<html lang="en">
<head>
<meta charset="utf-8">
<title>Get the Facts on Mpox Vaccination</title>
<link href="https://fonts.googleapis.com/css2?family=Bebas+Neue&family=Montserrat:wght@600&family=Source+Sans+3:ital,wght@0,400;0,700;1,400&display=swap" rel="stylesheet">
<style>
:root{
  --red:#b45b51;
  --teal:#4f8e8c;
  --teal-light:#53a7b1;
  --band:#588f8e;
  --ink:#1d1d1d;
  --cream:#f6f1e4;
  --cream-light:#fbf9f4;
  --link:#1f35d1;
  --green:#a9b873;
}
*{margin:0;padding:0;box-sizing:border-box}
html,body{width:1200px;height:893px;overflow:hidden;background:#fff}
body{position:relative;font-family:"Source Sans 3",sans-serif;color:var(--ink)}
.page{position:absolute;top:82px;width:509px;height:724px;overflow:hidden}
.page--front{left:77px;background:linear-gradient(90deg,var(--cream) 0%,var(--cream-light) 45%,var(--cream-light) 100%)}
.page--back{left:609px;background:linear-gradient(90deg,var(--cream-light) 0%,var(--cream-light) 55%,#eee6cf 100%)}
.side-curve{position:absolute;left:0;top:0}
.brand{position:absolute;left:39px;top:27px;display:flex;align-items:center;gap:12px}
.brand__mark{width:40px;height:40px;background:var(--teal-light)}
.brand__name{font-family:"Bebas Neue",sans-serif;font-size:20px;line-height:19px;color:var(--teal-light);letter-spacing:.3px}
.tagline{position:absolute;left:38px;top:84px;font-family:"Montserrat",sans-serif;font-weight:600;font-size:17.5px;color:var(--red);letter-spacing:.2px}
.title{position:absolute;left:38px;top:111px;font-family:"Bebas Neue",sans-serif;font-weight:400;color:var(--teal);font-size:45px;line-height:44px;letter-spacing:-.6px;white-space:nowrap}
.title__hl{background:var(--red);color:#fff;padding:0 4px}
.title__big{position:absolute;left:37px;top:152px;font-family:"Bebas Neue",sans-serif;color:var(--red);font-size:80px;line-height:70px;letter-spacing:.5px}
.beading-art{position:absolute;left:299px;top:224px;width:178px;height:178px;border-radius:50%;
  background:radial-gradient(circle at 50% 45%,#f7d26a 0%,#f0b54a 40%,#7fa39b 70%,#6f9553 82%,var(--green) 90%,#b77a6f 100%)}
.copy{position:absolute;font-size:11.6px;line-height:15.3px}
.copy p{margin:0}
.copy strong{font-weight:700}
.pin{display:inline-block;width:10px;height:10px;vertical-align:-1px;margin-right:3px}
.copy--intro{left:36px;top:231px;width:252px;font-size:11.2px}
.copy--risk{left:36px;top:436px;width:440px;line-height:16.2px}
.copy--risk .sub{padding-left:32px}
.border-stripe{position:absolute;left:0;top:685px;width:509px;height:5px;background:var(--red)}
.border-pattern{position:absolute;left:0;top:692px;width:509px;height:30px;
  background:linear-gradient(180deg,#74b3b6 0%,#c9c4b6 50%,#c97a6f 100%)}
.border-line{position:absolute;left:0;top:722px;width:509px;height:2px;background:var(--teal-light)}
.facts{position:absolute;left:39px;width:430px;font-size:11.8px;line-height:16.2px}
.facts h3{font-size:12px;font-weight:700;letter-spacing:.1px}
.facts .sub{padding-left:35px}
.facts a{color:var(--link)}
.info-band{position:absolute;left:0;top:569px;width:509px;height:41px;background:var(--band);color:#fff;font-weight:700;font-size:12.2px;line-height:15px;text-align:center;padding-top:5px}
.info-band a{color:#fff;text-decoration:none;margin:0 6px}
.funding{position:absolute;left:52px;top:627px;width:406px;height:68px;border:2px solid var(--red);background:#fff;padding:9px 7px 0 7px;font-size:6.4px;line-height:9.3px;text-align:justify}
</style>
</head>
<body>

<section class="page page--front">
  <svg class="side-curve" width="509" height="724" viewBox="0 0 509 724" aria-hidden="true">
    <defs>
      <linearGradient id="curveFill" x1="0" y1="0" x2="0" y2="1">
        <stop offset="0" stop-color="#4fa8b3"/>
        <stop offset=".55" stop-color="#5b8f92"/>
        <stop offset="1" stop-color="#b8675c"/>
      </linearGradient>
    </defs>
    <path d="M399 0 H509 V392 C462 335 424 258 420 180 C417 100 412 42 399 0 Z" fill="url(#curveFill)"/>
  </svg>

  <div class="brand">
    <div class="brand__mark"></div>
    <div class="brand__name">Worldwide Council for<br>Native Elders</div>
  </div>

  <div class="tagline">SHELTER IS KINDRED WARMTH</div>
  <h1 class="title">GET THE <span class="title__hl">FACTS ON</span> MPOX</h1>
  <div class="title__big">VACCINATION</div>

  <div class="beading-art" role="img" aria-label="Circular illustration of three people beading together at a table, framed by a braided sweetgrass ring"></div>

  <div class="copy copy--intro">
    <p><strong>FACT: MPOX (FORMERLY KNOWN AS MONKEYPOX) IS A SERIOUS VIRUS THAT CAN CAUSE RASH, FEVER, AND OTHER SYMPTOMS.</strong></p>
    <p><svg class="pin" viewBox="0 0 10 10"><path d="M6 0 L10 4 L8.5 4.6 L6.8 6.3 L7 8.4 L5.8 8.6 L3.8 6.6 L1 9.6 L.4 9 L3.4 6.2 L1.4 4.2 L1.6 3 L3.7 3.2 L5.4 1.5 Z" fill="#111"/></svg>Mpox can spread to anyone through close, personal, often skin-to-skin contact.</p>
    <p><strong>FACT: VACCINES CAN HELP KEEP YOURSELF, FAMILY, AND COMMUNITY SAFE BY STOPPING THE SPREAD OF MPOX.</strong></p>
    <p><svg class="pin" viewBox="0 0 10 10"><path d="M6 0 L10 4 L8.5 4.6 L6.8 6.3 L7 8.4 L5.8 8.6 L3.8 6.6 L1 9.6 L.4 9 L3.4 6.2 L1.4 4.2 L1.6 3 L3.7 3.2 L5.4 1.5 Z" fill="#111"/></svg>Vaccines are important in stopping the spread of mpox. People who are vaccinated for mpox should still continue to avoid close, skin-to-skin contact with someone who has mpox.</p>
  </div>

  <div class="copy copy--risk">
    <p><strong>FACT: THE BITS RECOMMENDS GETTING A VACCINE FOR PEOPLE 18 AND OLDER WHO ARE AT RISK FOR MPOX.</strong></p>
    <p><svg class="pin" viewBox="0 0 10 10"><path d="M6 0 L10 4 L8.5 4.6 L6.8 6.3 L7 8.4 L5.8 8.6 L3.8 6.6 L1 9.6 L.4 9 L3.4 6.2 L1.4 4.2 L1.6 3 L3.7 3.2 L5.4 1.5 Z" fill="#111"/></svg>People at risk for mpox include:</p>
    <p>• Gay, bisexual, Two Spirit, MSM (men who have sex with men), trans or gender diverse people who in the past 6 months have had one of the following:</p>
    <p class="sub">▪ A new diagnosis of more than one sexually transmitted disease</p>
    <p class="sub">▪ More than one sex partner</p>
    <p class="sub">▪ Sex at a commercial sex venue</p>
    <p class="sub">▪ Sex at a large public event where there are people who have mpox</p>
    <p>• Sexual partners of persons with the risks described in above</p>
    <p>• People who experience any of the above</p>
    <p><strong>FACT: PEOPLE WITH UNTREATED HIV ARE MORE LIKELY TO GET SEVERE CASES OF MPOX.</strong></p>
    <p><svg class="pin" viewBox="0 0 10 10"><path d="M6 0 L10 4 L8.5 4.6 L6.8 6.3 L7 8.4 L5.8 8.6 L3.8 6.6 L1 9.6 L.4 9 L3.4 6.2 L1.4 4.2 L1.6 3 L3.7 3.2 L5.4 1.5 Z" fill="#111"/></svg>The mpox vaccine is safe for people with HIV. Get two doses of the mpox vaccine as soon as you can. If you don't know your HIV status, get tested.</p>
  </div>

  <div class="border-stripe"></div>
  <div class="border-pattern" role="img" aria-label="Woven zigzag border pattern in teal and red"></div>
  <div class="border-line"></div>
</section>

<section class="page page--back">
  <div class="facts" style="top:47px">
    <h3>FACT: TWO SHOTS ARE BETTER THAN ONE.</h3>
    <p><svg class="pin" viewBox="0 0 10 10"><path d="M6 0 L10 4 L8.5 4.6 L6.8 6.3 L7 8.4 L5.8 8.6 L3.8 6.6 L1 9.6 L.4 9 L3.4 6.2 L1.4 4.2 L1.6 3 L3.7 3.2 L5.4 1.5 Z" fill="#111"/></svg> VAXORA is a 2-dose vaccine that protects against mpox infections.</p>
    <p><svg class="pin" viewBox="0 0 10 10"><path d="M6 0 L10 4 L8.5 4.6 L6.8 6.3 L7 8.4 L5.8 8.6 L3.8 6.6 L1 9.6 L.4 9 L3.4 6.2 L1.4 4.2 L1.6 3 L3.7 3.2 L5.4 1.5 Z" fill="#111"/></svg> People need to get both doses of the vaccine for the best protection against mpox, <em>unless you had a severe allergic reaction after getting your first dose of the VAXORA vaccine.</em></p>
    <p><svg class="pin" viewBox="0 0 10 10"><path d="M6 0 L10 4 L8.5 4.6 L6.8 6.3 L7 8.4 L5.8 8.6 L3.8 6.6 L1 9.6 L.4 9 L3.4 6.2 L1.4 4.2 L1.6 3 L3.7 3.2 L5.4 1.5 Z" fill="#111"/></svg> The second dose should be given 4 weeks after the first dose.</p>
  </div>

  <div class="facts" style="top:162px">
    <h3>FACT: ALREADY EXPOSED TO MPOX? YOU CAN STILL GET VACCINATED.</h3>
    <p><svg class="pin" viewBox="0 0 10 10"><path d="M6 0 L10 4 L8.5 4.6 L6.8 6.3 L7 8.4 L5.8 8.6 L3.8 6.6 L1 9.6 L.4 9 L3.4 6.2 L1.4 4.2 L1.6 3 L3.7 3.2 L5.4 1.5 Z" fill="#111"/></svg> Get vaccinated as soon as possible after being exposed to someone with mpox (if exposed less than 14 days ago, ideally within 4 days of exposure).</p>
  </div>

  <div class="facts" style="top:227px">
    <h3>FACT: YOU CAN CALL THE SHOTS.</h3>
    <p><svg class="pin" viewBox="0 0 10 10"><path d="M6 0 L10 4 L8.5 4.6 L6.8 6.3 L7 8.4 L5.8 8.6 L3.8 6.6 L1 9.6 L.4 9 L3.4 6.2 L1.4 4.2 L1.6 3 L3.7 3.2 L5.4 1.5 Z" fill="#111"/></svg> Reduce scarring by asking about how and where to get the mpox vaccine on your body, such as on the back of your upper arm.</p>
  </div>

  <div class="facts" style="top:293px">
    <h3>FACT: NOT EVERYONE HAS SIDE EFFECTS, BUT SOME PEOPLE DO.</h3>
    <p><svg class="pin" viewBox="0 0 10 10"><path d="M6 0 L10 4 L8.5 4.6 L6.8 6.3 L7 8.4 L5.8 8.6 L3.8 6.6 L1 9.6 L.4 9 L3.4 6.2 L1.4 4.2 L1.6 3 L3.7 3.2 L5.4 1.5 Z" fill="#111"/></svg>The most common side effects after the VAXORA vaccine are:</p>
    <p class="sub">• Pain, redness, and itching at the spot the vaccine is given</p>
    <p class="sub">• Fever, headache, tiredness, nausea, chills, and muscle aches</p>
    <p><svg class="pin" viewBox="0 0 10 10"><path d="M6 0 L10 4 L8.5 4.6 L6.8 6.3 L7 8.4 L5.8 8.6 L3.8 6.6 L1 9.6 L.4 9 L3.4 6.2 L1.4 4.2 L1.6 3 L3.7 3.2 L5.4 1.5 Z" fill="#111"/></svg>These area signs that your immune system is responding, not that you are getting sick.</p>
  </div>

  <div class="facts" style="top:407px">
    <h3>FACT: MPOX VACCINES ARE FREE.</h3>
    <p><svg class="pin" viewBox="0 0 10 10"><path d="M6 0 L10 4 L8.5 4.6 L6.8 6.3 L7 8.4 L5.8 8.6 L3.8 6.6 L1 9.6 L.4 9 L3.4 6.2 L1.4 4.2 L1.6 3 L3.7 3.2 L5.4 1.5 Z" fill="#111"/></svg> Providers must give you the vaccine regardless of your ability to pay the administration fee. <a href="https://www.ravenkinship.org/vaccines">Learn more and find an mpox vaccine site near you.</a></p>
  </div>

  <div class="facts" style="top:473px">
    <h3>FACT: MPOX VACCINES ARE SAFE AND EFFECTIVE.</h3>
    <p><svg class="pin" viewBox="0 0 10 10"><path d="M6 0 L10 4 L8.5 4.6 L6.8 6.3 L7 8.4 L5.8 8.6 L3.8 6.6 L1 9.6 L.4 9 L3.4 6.2 L1.4 4.2 L1.6 3 L3.7 3.2 L5.4 1.5 Z" fill="#111"/></svg> Over one million vaccine doses have been given in Northland with no new or unexpected safety concerns and serious adverse events to the mpox vaccine are rare. People who have been vaccinated can still get mpox, <a href="https://www.nwho.example/poxvirus/mpox/">but vaccination may make illness less severe.</a></p>
  </div>

  <div class="info-band">
    For more information, please visit: <a href="https://www.ravenkinship.org/vaccines">www.ravenkinship.org/vaccines</a><br>
    <a href="https://www.bolderpath.org/campaigns/mpox/">www.bolderpath.org/campaigns/mpox/</a> <a href="https://www.nwho.example/poxvirus/mpox/">www.nwho.example/poxvirus/mpox/</a>
  </div>

  <div class="funding">"This project: Joining Hands with Regional Allies to Strengthen Neighborhood-Led Groups to Broaden Immunization Reach Among Diverse Cultural and Heritage Grown-Up Groups Presently Facing Gaps is supported by the Bureau for Illness Tracking and Safeguarding (BITS) of the Federal Office of Wellness and Social Services (OWS) as part of a financial assistance award totaling $5,000,000 with 100 percent funded by BITS/OWS. The contents are those of the author(s) and do not necessarily represent the official views of, nor an endorsement by, BITS/OWS or the Northland Federal Government. "</div>
</section>

</body>
</html>
```